Packaging box design (uLumo style)

To create a striking but minimalist box for a new tool handle. The top sleeve external box dimensions are L230xW85xH65mm. We will need the logo (plia by KVR), you can use any of our rendered drawings if you feel it would look good. Information to be included; Ergonomic Adjustable Handle / 12 position lock system / Quick release shaft / Weight and space saving / Comfort grip / Ability to convert existing toolsFor purchase and converting options please visit (USA) www.brasolmark.com or (Europe) www.kvrtools.com.

Target Market(s)

Automotive professionals

Font styles to use
Sans Serif

Colors
fbed22
333333
5c5c5c
9d9d9d

Requirements
Must have
• Logo - plia by KVR (attached)

```html
<!DOCTYPE html>
<html lang="en">
<head>
<meta charset="utf-8">
<title>plia series by KVR – packaging</title>
<link rel="stylesheet" href="https://fonts.googleapis.com/css2?family=Poppins:wght@600&family=Noto+Serif:ital@1&display=swap">
<style>
  :root {
    --bg: #e6e6e6;
    --yellow: #fbed22;
    --ink: #333333;
    --mid: #5c5c5c;
    --light: #9d9d9d;
    --white: #ffffff;
    --gold-a: #e3c45a;
    --gold-b: #a7882d;
  }
  html, body { margin: 0; padding: 0; overflow: hidden; }
  body { background: var(--bg); }
  .canvas {
    position: relative;
    width: 1200px;
    height: 931px;
    overflow: hidden;
    background: var(--bg);
  }
  .panel {
    position: absolute;
    box-sizing: border-box;
    outline: 1px solid #d4d4d4;
  }
  .panel--white { background: var(--white); }
  .panel--yellow { background: var(--yellow); }

  .panel--lid    { left: 347px; top: 100px; width: 506px; height: 187px; }
  .panel--front  { left: 347px; top: 287px; width: 506px; height: 143px; }
  .panel--end-l  { left: 160px; top: 287px; width: 187px; height: 143px; }
  .panel--end-r  { left: 853px; top: 287px; width: 187px; height: 143px; }
  .panel--info   { left: 347px; top: 430px; width: 506px; height: 187px; }
  .panel--rear   { left: 347px; top: 617px; width: 506px; height: 143px; }

  .wordmark {
    position: absolute;
    font-family: "Poppins", sans-serif;
    font-weight: 600;
    color: var(--ink);
    line-height: 1;
    white-space: nowrap;
  }
  .wordmark__name { display: block; }
  .wordmark__sub { display: block; margin-left: 36%; }

  .wordmark--large { font-size: 48px; }
  .wordmark--large .wordmark__sub { font-size: 17px; margin-top: 2px; }
  .wordmark--small { font-size: 24px; }
  .wordmark--small .wordmark__sub { font-size: 9px; margin-top: 1px; }

  .panel--front .wordmark { left: 150px; top: 34px; }
  .panel--rear .wordmark  { left: 150px; top: 34px; }
  .panel--end-l .wordmark,
  .panel--end-r .wordmark { left: 50px; top: 50px; }
  .panel--lid .wordmark--tiny { left: 410px; top: 20px; font-size: 14px; }
  .panel--lid .wordmark--tiny .wordmark__sub { font-size: 6px; }
  .panel--info .wordmark { left: 24px; top: 30px; }

  .product-render {
    position: absolute;
    left: 88px; top: 58px;
    width: 300px; height: 72px;
    border-radius: 40px 14px 14px 40px;
    background: linear-gradient(180deg, var(--gold-a), var(--gold-b));
  }

  .features {
    position: absolute;
    left: 180px; top: 28px;
    margin: 0; padding: 0;
    list-style: none;
    font-family: "Noto Serif", serif;
    font-style: italic;
    font-size: 11px;
    color: #1a1a1a;
  }
  .features li { position: relative; padding-left: 14px; margin-bottom: 9px; }
  .features li::before {
    content: ""; position: absolute; left: 0; top: 5px;
    width: 5px; height: 5px; border-radius: 50%; background: #1a1a1a;
  }

  .views { position: absolute; left: 372px; top: 26px; width: 116px; }
  .view__label {
    font-family: "Noto Serif", serif; font-style: italic; font-weight: 700;
    font-size: 7px; color: var(--ink); text-align: center; margin: 0 0 4px;
  }
  .view__drawing {
    height: 40px; margin-bottom: 20px;
    border: 1px solid var(--light); border-radius: 20px 6px 6px 20px;
    background: linear-gradient(180deg, #fafafa, #efefef);
  }
</style>
</head>
<body>
<main class="canvas">

  <section class="panel panel--white panel--lid">
    <div class="product-render" role="img" aria-label="Rendered gold adjustable tool handle with dark grip"></div>
    <div class="wordmark wordmark--tiny"><span class="wordmark__name">plia</span><span class="wordmark__sub">series by KVR</span></div>
  </section>

  <section class="panel panel--white panel--end-l">
    <div class="wordmark wordmark--small"><span class="wordmark__name">plia</span><span class="wordmark__sub">series by KVR</span></div>
  </section>

  <section class="panel panel--yellow panel--front">
    <div class="wordmark wordmark--large"><span class="wordmark__name">plia</span><span class="wordmark__sub">series by KVR</span></div>
  </section>

  <section class="panel panel--white panel--end-r">
    <div class="wordmark wordmark--small"><span class="wordmark__name">plia</span><span class="wordmark__sub">series by KVR</span></div>
  </section>

  <section class="panel panel--white panel--info">
    <div class="wordmark wordmark--small"><span class="wordmark__name">plia</span><span class="wordmark__sub">series by KVR</span></div>
    <ul class="features">
      <li>Ergonomic Adjustable Handle</li>
      <li>12 position lock system</li>
      <li>Quick release shaft</li>
      <li>Weight and space saving</li>
      <li>Comfort grip</li>
      <li>Ability to convert existing tools</li>
    </ul>
    <div class="views">
      <p class="view__label">Top View</p>
      <div class="view__drawing" role="img" aria-label="Line drawing of the handle seen from above"></div>
      <p class="view__label">Side View</p>
      <div class="view__drawing" role="img" aria-label="Line drawing of the handle seen from the side"></div>
    </div>
  </section>

  <section class="panel panel--yellow panel--rear">
    <div class="wordmark wordmark--large"><span class="wordmark__name">plia</span><span class="wordmark__sub">series by KVR</span></div>
  </section>

</main>
</body>
</html>
```